Business Card for a recruitment agency specializing in engineers and geeks.

I am looking to create Business Card Design for my company.
That
## Company name:
Quorvant Inc.
Quorvant is a term coined from the following concepts.
1. geek + engineer
2. geek utopia
## Company Description:
The concept of the company is to be a recruitment agency that creates a paradise for geeky engineers. We want to be a place where engineers can have more freedom and ideal career support.
# Target.
The noun itself is often given to companies that want to hire engineers, geeks, and IT-related personnel, so it would be nice to get the impression that this company seems to have good engineers and IT personnel. There are many occasions where I meet with the human resources department, president, or senior management and give it to them.
# Atmosphere
We are happy with simplicity, but with an impact that will help people remember the company. The logo is based on a dinosaur that does programming, so it should be somewhat playful, but since it will basically be used in a business setting, please don't make it too silly.
# About the logo
See the attached files. The company logo represents our engineers smiling upward because of our work, with the motif of a dinosaur doing programming.
## Color
We will leave the color scheme to you, but since the logo is in black and white, colors with such a taste would fit well.
## file format
ai, psd, png, svg
Industry/Entity Type
human resource and employment agency
Contact Information for Business Card
Company name, address, email, tel, URL,logo
Colors
Designer to choose colors to be used in the design.

```html
<!DOCTYPE html>
<html lang="en">
<head>
<meta charset="utf-8">
<title>Quorvant Inc. — Business Card</title>
<link href="https://fonts.googleapis.com/css2?family=Roboto:wght@400;500;700&display=swap" rel="stylesheet">
<style>
  :root {
    --page: #2b2b2c;
    --card-top: #1b1b1c;
    --card-bottom: #2c2c2e;
    --gloss: #4d4d50;
    --text-light: #f0f0f0;
    --text-soft: #d2d2d2;
    --rule: #9a9a9a;
    --band-grey: #8c8c8c;
    --band-light: #e6e6e6;
    --band-text: #1e1e1e;
  }
  * { box-sizing: border-box; margin: 0; padding: 0; }
  html, body { width: 1200px; height: 1138px; overflow: hidden; }
  body {
    background: var(--page);
    font-family: "Roboto", Arial, sans-serif;
    position: relative;
  }
  .card {
    position: absolute;
    left: 290px;
    width: 620px;
    height: 375px;
    border-radius: 16px;
    overflow: hidden;
    background: linear-gradient(160deg, var(--card-top), var(--card-bottom));
  }
  .card--front { top: 186px; }
  .card--back { top: 608px; }

  /* Front */
  .front-pattern {
    position: absolute; inset: 0;
    background: linear-gradient(160deg, #1e1e1f, #2a2a2c);
  }
  .front-brand {
    position: absolute; left: 0; right: 0; top: 150px;
    display: flex; align-items: center; justify-content: center; gap: 18px;
  }
  .front-brand__square {
    width: 44px; height: 44px; background: var(--gloss);
  }
  .front-brand__name {
    font-weight: 500; font-size: 54px; line-height: 1;
    color: var(--gloss); letter-spacing: 1px;
  }
  .front-url {
    position: absolute; left: 0; right: 0; top: 334px;
    display: flex; align-items: center; justify-content: center; gap: 14px;
    font-size: 15px; color: var(--text-soft); letter-spacing: .3px;
  }
  .front-url__rule { width: 62px; height: 2px; background: var(--rule); }

  /* Back */
  .back-brand {
    position: absolute; left: 28px; top: 66px;
    display: flex; align-items: center; gap: 16px;
  }
  .back-brand__square { width: 38px; height: 38px; background: var(--text-light); }
  .back-brand__name {
    font-weight: 500; font-size: 40px; line-height: 1;
    color: var(--text-light); letter-spacing: 1px;
  }
  .person { position: absolute; left: 27px; top: 208px; }
  .person__name { font-weight: 700; font-size: 22px; color: var(--text-light); }
  .person__title { font-size: 15px; color: var(--text-soft); margin-top: 5px; }
  .address {
    position: absolute; left: 27px; top: 292px;
    font-size: 15px; line-height: 24px; color: var(--text-soft);
  }
  .contacts {
    position: absolute; left: 326px; top: 220px;
    list-style: none; font-size: 15px; color: var(--text-soft);
  }
  .contacts li { display: flex; align-items: center; height: 24px; }
  .contacts svg { width: 14px; height: 14px; margin-right: 19px; fill: var(--text-soft); }
  .bottom-band { position: absolute; left: 0; bottom: 0; width: 620px; height: 46px; }
  .slogan {
    position: absolute; left: 328px; top: 342px;
    font-size: 15px; color: var(--band-text);
  }
</style>
</head>
<body>

<section class="card card--front">
  <div class="front-pattern" role="img" aria-label="Faint repeating brand-mark pattern across the card"></div>
  <div class="front-brand">
    <span class="front-brand__square"></span>
    <span class="front-brand__name">Quorvant</span>
  </div>
  <div class="front-url">
    <span class="front-url__rule"></span>
    <span>www.quorvant.com</span>
    <span class="front-url__rule"></span>
  </div>
</section>

<section class="card card--back">
  <div class="back-brand">
    <span class="back-brand__square"></span>
    <span class="back-brand__name">Quorvant</span>
  </div>

  <div class="person">
    <div class="person__name">Evan Holloway</div>
    <div class="person__title">Managing Director</div>
  </div>

  <div class="address">234 Anywhere St., Any City,<br>Any Town, US 123456</div>

  <ul class="contacts">
    <li>
      <svg viewBox="0 0 16 16"><path d="M2 6c0-2 3-3.5 6-3.5S14 4 14 6v1h-3V5.5H5V7H2z"/><rect x="3" y="8" width="10" height="6" rx="1"/></svg>
      000-222-3333
    </li>
    <li>
      <svg viewBox="0 0 16 16"><path d="M1 3h14v10H1z M2.5 4.5 8 9l5.5-4.5v7h-11z" fill-rule="evenodd"/></svg>
      evan@quorvant.com
    </li>
    <li>
      <svg viewBox="0 0 16 16"><circle cx="8" cy="8" r="6.5" fill="none" stroke="#d2d2d2" stroke-width="1.4"/><path d="M1.5 8h13M8 1.5v13" stroke="#d2d2d2" stroke-width="1.2"/><ellipse cx="8" cy="8" rx="3" ry="6.5" fill="none" stroke="#d2d2d2" stroke-width="1.2"/></svg>
      www.quorvant.com
    </li>
  </ul>

  <svg class="bottom-band" viewBox="0 0 620 46" preserveAspectRatio="none">
    <rect x="0" y="33" width="275" height="13" fill="var(--band-grey)"/>
    <path d="M292 1 H620 V46 H264 L282 6 Q284 1 292 1 Z" fill="var(--band-light)"/>
  </svg>
  <div class="slogan">Quorvant Slogan is Here</div>
</section>

</body>
</html>
```